Dermatology Office Business Card Update

Updating some information on the current business card. Do not adjust font type. Need both rounded rectangle and rounded square card files. In addition, must have separate file for both rectangle and square cards for gold foil printing.1. Update phone number with: 555-301-2846. Remove email address3. Add this website to be listed under clearhavenskinclinic.com:jilluxe.com4. Under updated phone number, add the photolake logo in color and then a space and the following text: @skinbymona. Gold foil should be inclusive of the outline of the butterfly wings on the front. Also should put a small hyphen that is also gold foil under the cursive Mona Perlow, MD and before the block lettering begins.Back of card remains the samePlease feel free to contact me with any questions!

Patients

Just needs some updates along with files for gold foil printing

• Updating some information on the current business card. Do not adjust font type. Need both rounded rectangle and rounded square card files. In addition, must have separate file for both rectangle and square cards for gold foil printing.
• 1. Update phone number with: 555-301-2846
• 2. Remove email address
• 3. Add this website to be listed under clearhavenskinclinic.com:
• monavea.com
• 4. Under updated phone number, add the photolake logo in color and then a space and the following text: @skinbymona
• 5. Gold foil should be inclusive of the outline of the butterfly wings on the front. Also should put a small hyphen that is also gold foil under the cursive Mona Perlow, MD and before the block lettering begins.
• Back of card remains the same
• Please feel free to contact me with any questions!

```html
<!DOCTYPE html>
<html lang="en">
<head>
<meta charset="utf-8">
<title>Mona Perlow, MD – Business Cards</title>
<link rel="stylesheet" href="https://fonts.googleapis.com/css2?family=Montserrat:wght@400;500;700;800&display=swap">
<style>
  :root {
    --canvas: #e9e7ea;
    --card-white: #ffffff;
    --navy: #3e4b66;
    --navy-soft: #56627c;
    --rose: #d8b4b6;
    --gold: #c9a24a;
    --gold-light: #e6cd82;
    --back-rose: #a07c85;
    --back-mauve: #8b7590;
    --back-blue: #45608f;
    --white: #ffffff;
  }
  * { box-sizing: border-box; margin: 0; padding: 0; }
  html, body {
    width: 1200px; height: 900px; overflow: hidden;
    background: var(--canvas);
    font-family: "Montserrat", sans-serif;
  }
  .stage { position: relative; width: 1200px; height: 900px; }

  .card {
    position: absolute;
    border-radius: 14px;
    overflow: hidden;
    box-shadow: 0 10px 28px rgba(40, 30, 50, 0.18);
  }
  .card--rect { width: 540px; height: 309px; top: 40px; }
  .card--square { width: 440px; height: 440px; top: 420px; }
  .card--rect.card-back { left: 40px; }
  .card--rect.card-front { left: 620px; }
  .card--square.card-back { left: 140px; }
  .card--square.card-front { left: 620px; }

  /* Back */
  .card-back {
    background:
      radial-gradient(ellipse at 20% 70%, rgba(170,130,138,0.9), transparent 60%),
      linear-gradient(120deg, var(--back-rose) 0%, var(--back-rose) 35%, var(--back-mauve) 70%, var(--back-blue) 100%);
    display: flex; flex-direction: column; align-items: center; justify-content: center;
    gap: 20px;
  }
  .card-back .brand-mark {
    width: 60px; height: 60px; border-radius: 50%;
    background: var(--white); opacity: 0.92;
  }
  .card--square.card-back .brand-mark { width: 80px; height: 80px; }
  .card-back .brand-name {
    color: var(--white);
    font-size: 13px; font-weight: 500;
    letter-spacing: 0.42em; padding-left: 0.42em;
    text-transform: uppercase;
  }

  /* Front */
  .card-front { background: var(--card-white); }
  .front-brand {
    position: absolute; left: 0; right: 0;
    display: flex; flex-direction: column; align-items: center; gap: 16px;
  }
  .front-brand .brand-mark { border-radius: 50%; background: var(--rose); }
  .front-brand .brand-name {
    color: var(--navy-soft);
    font-size: 13px; font-weight: 500;
    letter-spacing: 0.42em; padding-left: 0.42em;
    text-transform: uppercase;
  }
  .holder {
    position: absolute;
    display: flex; flex-direction: column; gap: 8px;
  }
  .holder-name {
    color: var(--navy);
    font-size: 20px; font-weight: 800;
    letter-spacing: 0.02em;
    text-transform: uppercase;
    white-space: nowrap;
  }
  .foil-hyphen {
    width: 26px; height: 3px; border-radius: 2px;
    background: linear-gradient(90deg, var(--gold), var(--gold-light));
  }
  .contact-list {
    position: absolute;
    list-style: none;
    display: flex; flex-direction: column; gap: 8px;
    color: var(--navy);
    font-size: 12px; font-weight: 500;
  }
  .contact-list li { display: flex; align-items: center; gap: 8px; height: 15px; white-space: nowrap; }
  .contact-list svg { width: 12px; height: 12px; flex: none; }
  .social-dot {
    width: 10px; height: 10px; border-radius: 2px;
    background: var(--rose); flex: none; margin: 0 1px;
  }
  .divider { position: absolute; background: var(--navy-soft); opacity: 0.7; }
  .gold-band {
    position: absolute; left: 0; right: 0; height: 6px;
    background: linear-gradient(90deg, var(--gold), var(--gold-light), var(--gold));
  }

  /* Rectangle front layout */
  .card--rect .front-brand { top: 34px; }
  .card--rect .front-brand .brand-mark { width: 66px; height: 66px; }
  .card--rect .holder { left: 36px; top: 200px; }
  .card--rect .divider { left: 300px; top: 160px; width: 1px; height: 96px; }
  .card--rect .contact-list { left: 316px; top: 162px; }
  .card--rect .gold-band { bottom: 22px; }

  /* Square front layout */
  .card--square .front-brand { top: 46px; }
  .card--square .front-brand .brand-mark { width: 80px; height: 80px; }
  .card--square .holder { left: 0; right: 0; top: 196px; align-items: center; }
  .card--square .divider { left: 150px; top: 258px; width: 140px; height: 1px; }
  .card--square .contact-list { left: 130px; top: 276px; }
  .card--square .gold-band { bottom: 26px; }
</style>
</head>
<body>
<main class="stage">
  <!-- Rectangle cards -->
  <section class="card card--rect card-back" aria-label="Back of rectangle card">
    <div class="brand-mark" aria-hidden="true"></div>
    <p class="brand-name">Evolving Self</p>
  </section>

  <section class="card card--rect card-front" aria-label="Front of rectangle card">
    <div class="front-brand">
      <div class="brand-mark" aria-hidden="true"></div>
      <p class="brand-name">Evolving Self</p>
    </div>
    <div class="holder">
      <h1 class="holder-name">Mona Perlow, MD</h1>
      <div class="foil-hyphen" aria-hidden="true"></div>
    </div>
    <div class="divider"></div>
    <ul class="contact-list">
      <li>
        <svg viewBox="0 0 24 24" aria-hidden="true"><path fill="#3e4b66" d="M6.6 10.8a15.2 15.2 0 0 0 6.6 6.6l2.2-2.2c.3-.3.7-.4 1-.2 1.1.4 2.3.6 3.6.6.6 0 1 .4 1 1V20c0 .6-.4 1-1 1A17 17 0 0 1 3 4c0-.6.4-1 1-1h3.5c.6 0 1 .4 1 1 0 1.3.2 2.5.6 3.6.1.3 0 .7-.2 1z"/></svg>
        <span>555-301-2846</span>
      </li>
      <li><span class="social-dot" aria-hidden="true"></span><span>@skinbymona</span></li>
      <li>
        <svg viewBox="0 0 24 24" aria-hidden="true"><circle cx="12" cy="12" r="9" fill="none" stroke="#3e4b66" stroke-width="2.4"/><path d="M3 12h18M12 3c3 3 3 15 0 18M12 3c-3 3-3 15 0 18" fill="none" stroke="#3e4b66" stroke-width="1.6"/></svg>
        <span>clearhavenskinclinic.com</span>
      </li>
      <li>
        <svg viewBox="0 0 24 24" aria-hidden="true"><circle cx="12" cy="12" r="9" fill="none" stroke="#3e4b66" stroke-width="2.4"/><path d="M3 12h18M12 3c3 3 3 15 0 18M12 3c-3 3-3 15 0 18" fill="none" stroke="#3e4b66" stroke-width="1.6"/></svg>
        <span>monavea.com</span>
      </li>
    </ul>
    <div class="gold-band"></div>
  </section>

  <!-- Square cards -->
  <section class="card card--square card-back" aria-label="Back of square card">
    <div class="brand-mark" aria-hidden="true"></div>
    <p class="brand-name">Evolving Self</p>
  </section>

  <section class="card card--square card-front" aria-label="Front of square card">
    <div class="front-brand">
      <div class="brand-mark" aria-hidden="true"></div>
      <p class="brand-name">Evolving Self</p>
    </div>
    <div class="holder">
      <h2 class="holder-name">Mona Perlow, MD</h2>
      <div class="foil-hyphen" aria-hidden="true"></div>
    </div>
    <div class="divider"></div>
    <ul class="contact-list">
      <li>
        <svg viewBox="0 0 24 24" aria-hidden="true"><path fill="#3e4b66" d="M6.6 10.8a15.2 15.2 0 0 0 6.6 6.6l2.2-2.2c.3-.3.7-.4 1-.2 1.1.4 2.3.6 3.6.6.6 0 1 .4 1 1V20c0 .6-.4 1-1 1A17 17 0 0 1 3 4c0-.6.4-1 1-1h3.5c.6 0 1 .4 1 1 0 1.3.2 2.5.6 3.6.1.3 0 .7-.2 1z"/></svg>
        <span>555-301-2846</span>
      </li>
      <li><span class="social-dot" aria-hidden="true"></span><span>@skinbymona</span></li>
      <li>
        <svg viewBox="0 0 24 24" aria-hidden="true"><circle cx="12" cy="12" r="9" fill="none" stroke="#3e4b66" stroke-width="2.4"/><path d="M3 12h18M12 3c3 3 3 15 0 18M12 3c-3 3-3 15 0 18" fill="none" stroke="#3e4b66" stroke-width="1.6"/></svg>
        <span>clearhavenskinclinic.com</span>
      </li>
      <li>
        <svg viewBox="0 0 24 24" aria-hidden="true"><circle cx="12" cy="12" r="9" fill="none" stroke="#3e4b66" stroke-width="2.4"/><path d="M3 12h18M12 3c3 3 3 15 0 18M12 3c-3 3-3 15 0 18" fill="none" stroke="#3e4b66" stroke-width="1.6"/></svg>
        <span>monavea.com</span>
      </li>
    </ul>
    <div class="gold-band"></div>
  </section>
</main>
</body>
</html>
```